WordPress Website for Accounting Firm

I have attached an excel sheet showing what i need done for my accounting website. Currently i have a WP website but its not live and do not like it. I can give a link if that will help. Total pages is around 12. I can buy and supply the images but have provided indication of what i want in the excel. I will need the designer to do the coding to make the website fully functional. I want a clean look and attractive. Don't want too dark colors. Once i like the landing page, i will need the designer to code code the website. Just want to look first. I will provide the logo file and put the contents myself. Just put dummy contents for now to show how it will look.
Updates
Can you please use the attached images so i can see how nit will look on the coverage as an option. These are from pixelharbor
264918053
418273596
1537206419
1096382147
Currently there are only 2 provided by myself as Photo 1 and Photo 2
Many Thanks!
Industry/Entity Type
Accounting and Finance
Number of Pages Required
5+ page

```html
<!DOCTYPE html>
<html lang="en">
<head>
<meta charset="utf-8">
<title>Harbourline Tax Solutions</title>
<link rel="stylesheet" href="https://fonts.googleapis.com/css2?family=Lato:ital,wght@0,400;0,700;0,900;1,400&family=Poppins:wght@600&family=Montserrat:wght@600;700&display=swap">
<style>
:root{
  --green:#4a9b3f;
  --green-dark:#3f8a35;
  --ink:#1b1b1b;
  --body:#6a6a6a;
  --black:#000;
  --white:#fff;
  --hero-a:#0b1f1a;
  --hero-b:#1f4a3f;
}
*{margin:0;padding:0;box-sizing:border-box}
html,body{width:1200px;height:3509px;overflow:hidden}
body{position:relative;background:var(--white);font-family:'Lato',sans-serif;color:var(--ink)}
.abs{position:absolute}

/* header */
.site-header{left:0;top:0;width:1200px;height:98px;background:var(--green)}
.brand{left:109px;top:36px;color:var(--white);font-size:20px;font-weight:700;letter-spacing:.5px;line-height:26px}
.main-nav{left:505px;top:38px;display:flex;gap:28px;font-size:15px;color:var(--white)}
.main-nav a{color:inherit;text-decoration:none;padding-bottom:6px}
.main-nav a.active{border-bottom:3px solid var(--white)}
.search-btn{left:1038px;top:22px;width:52px;height:52px;border:2px solid var(--white);border-radius:50%}

/* hero */
.hero{left:0;top:98px;width:1200px;height:654px;background:radial-gradient(circle at 78% 40%,#3d6b55 0%,var(--hero-b) 30%,var(--hero-a) 75%)}
.hero-title{position:absolute;left:109px;top:158px;font-weight:900;font-size:70px;line-height:86px;color:var(--white)}
.btn{display:inline-flex;align-items:center;gap:6px;background:var(--green);color:var(--white);font-weight:700;font-size:15px;border-radius:22px;padding:0 24px;height:43px;text-decoration:none}
.hero .btn{position:absolute;left:109px;top:419px}
.dots{position:absolute;left:109px;top:541px;display:flex;gap:8px;align-items:center}
.dots span{width:12px;height:12px;border-radius:50%;background:var(--white)}
.dots span.on{width:18px;height:18px;background:var(--green)}

/* about */
.about-photo{left:154px;top:831px;width:404px;height:404px;border-radius:50%;background:linear-gradient(135deg,#c9c4bb,#8b6a4c 60%,#5b4534)}
.about-ring{left:124px;top:808px}
.about-title{left:606px;top:828px;font-size:39px;font-weight:700;letter-spacing:-.5px}
.about-title em{font-style:normal;color:var(--green)}
.about-copy{left:606px;top:888px;width:483px;font-size:14.5px;line-height:25.8px;color:var(--body);text-align:justify}
.about-copy p+p{margin-top:26px}
.about .btn{position:absolute;left:606px;top:1165px}

/* why */
.why{left:0;top:1311px;width:665px;height:556px;background:var(--green);color:var(--white)}
.why h2{position:absolute;left:111px;top:50px;font-size:39px;font-weight:700}
.why ul{position:absolute;left:111px;top:116px;width:520px;list-style:none;font-size:13px;line-height:19px}
.why li{position:relative;padding-left:26px;margin-bottom:19px}
.why li svg{position:absolute;left:0;top:3px}
.why-photo{left:665px;top:1311px;width:535px;height:556px;background:linear-gradient(135deg,#e9eaec,#cfd2d6 55%,#f3f3f3)}

/* testimonials */
.section-title{width:1200px;left:0;text-align:center;font-size:39px;font-weight:700;letter-spacing:-.5px}
.section-title em{font-style:normal;color:var(--green)}
.hand-left{left:129px;top:2021px;width:250px;height:300px;border-radius:40% 50% 45% 35%;background:linear-gradient(160deg,#f3d6c4,#e4b69c)}
.hand-right{left:845px;top:2040px;width:235px;height:384px;border-radius:45% 40% 30% 55%;background:linear-gradient(200deg,#f3d6c4,#e2b093)}
.tagline{left:380px;top:2090px;width:480px;text-align:center;font-family:'Poppins',sans-serif;font-weight:600;font-size:76px;line-height:70px;letter-spacing:-1px;z-index:2}
.tagline em{font-style:normal;color:var(--green)}
.quote{left:346px;top:2344px;width:508px;height:214px;background:var(--green);color:var(--white);text-align:center;padding:26px 44px 0}
.quote p{font-style:italic;font-size:13.5px;line-height:26px}
.quote h4{font-size:21px;font-weight:400;margin-top:10px}
.quote span{font-size:13.5px}
.arrow{top:2444px;font-size:22px;color:var(--ink)}

/* industries */
.industry{display:flex;align-items:center;gap:18px;font-size:14.5px;font-weight:700;color:var(--ink)}

/* footer */
.site-footer{left:0;top:3044px;width:1200px;height:465px;background:var(--black);color:var(--white)}
.subscribe{position:absolute;left:375px;top:70px;width:450px;height:42px;border-radius:21px;background:var(--white);border:2px solid var(--green)}
.subscribe span{position:absolute;left:34px;top:12px;font-size:13px;color:#777}
.subscribe b{position:absolute;right:2px;top:2px;width:146px;height:34px;border-radius:17px;background:var(--green);font-size:13px;line-height:34px;text-align:center}
.f-head{position:absolute;top:175px;font-family:'Montserrat',sans-serif;font-weight:700;font-size:22px}
.f-list{position:absolute;top:220px;list-style:none;font-family:'Montserrat',sans-serif;font-size:15px;line-height:28px;letter-spacing:.5px}
.f-list li{display:flex;gap:14px}
.f-list svg{flex:none;margin-top:8px}
.f-rule{position:absolute;top:177px;width:1px;height:150px;background:#666}
.socials{position:absolute;left:899px;top:218px;display:flex;gap:8px}
.socials span{width:39px;height:39px;border:1.5px solid var(--white);border-radius:50%}
.copyright{position:absolute;left:0;top:398px;width:1200px;text-align:center;font-family:'Montserrat',sans-serif;font-size:13.5px}
</style>
</head>
<body>

<header class="abs site-header">
  <div class="abs brand">HARBOURLINE TAX SOLUTIONS</div>
  <nav class="abs main-nav"><a class="active">HOME</a><a>SOLUTIONS</a><a>CLIENTS</a><a>CONTACT</a><a>CLIENT RESOURCES</a></nav>
  <div class="abs search-btn"><svg width="48" height="48" viewBox="0 0 48 48"><circle cx="23" cy="23" r="5" fill="none" stroke="#fff" stroke-width="2.2"/><line x1="27" y1="27" x2="31" y2="31" stroke="#fff" stroke-width="2.4"/></svg></div>
</header>

<section class="abs hero" role="img" aria-label="Glowing wireframe cube over a dark green network background">
  <h1 class="hero-title">HARBOURLINE<br>TAX<br>SOLUTIONS</h1>
  <a class="btn">GET STARTED <svg width="14" height="14" viewBox="0 0 14 14"><circle cx="7" cy="7" r="7" fill="#fff"/><path d="M6 4l3 3-3 3" fill="none" stroke="#4a9b3f" stroke-width="2"/></svg></a>
  <div class="dots"><span class="on"></span><span></span><span></span><span></span></div>
</section>

<section class="about">
  <svg class="abs about-ring" width="450" height="450" viewBox="0 0 450 450"><path d="M348 60 A222 222 0 1 0 348 390" fill="none" stroke="#4a9b3f" stroke-width="6"/></svg>
  <div class="abs about-photo" role="img" aria-label="Accountant working with a calculator at a wooden desk"></div>
  <h2 class="abs about-title">ABOUT <em>HARBOURLINE TAX</em></h2>
  <div class="abs about-copy">
    <p>Lorem ipsum dolor sit amet, consectetur adipiscing elit, sed do eiusmod tempor incididunt ut labore et dolore magna aliqua. Ut enim ad minim veniam, quis nostrud exercitation ullamco laboris nisi ut aliquip ex ea commodo consequat. Duis aute irure dolor in reprehenderit in voluptate velit esse cillum dolore eu fugiat nulla pariatur.</p>
    <p>Excepteur sint occaecat cupidatat non proident, sunt in culpa qui officia deserunt mollit anim id est laborum. Lorem ipsum dolor sit amet, consectetur adipiscing elit, sed do eiusmod tempor incididunt ut labore et dolore magna aliqua.</p>
  </div>
  <a class="btn">LEARN MORE <svg width="14" height="14" viewBox="0 0 14 14"><circle cx="7" cy="7" r="7" fill="#fff"/><path d="M6 4l3 3-3 3" fill="none" stroke="#4a9b3f" stroke-width="2"/></svg></a>
</section>

<section class="abs why">
  <h2>WHY CHOOSE US</h2>
  <ul>
    <li><svg width="13" height="13" viewBox="0 0 13 13"><circle cx="6.5" cy="6.5" r="5.5" fill="none" stroke="#fff" stroke-width="1.4"/><path d="M4 6.6l1.8 1.8L9.2 5" fill="none" stroke="#fff" stroke-width="1.4"/></svg>We specialise in accounting and tax solutions for all business structures and industries</li>
    <li><svg width="13" height="13" viewBox="0 0 13 13"><circle cx="6.5" cy="6.5" r="5.5" fill="none" stroke="#fff" stroke-width="1.4"/><path d="M4 6.6l1.8 1.8L9.2 5" fill="none" stroke="#fff" stroke-width="1.4"/></svg>Our team are qualified professionals with 50+ years of combined experience in CA industry</li>
    <li><svg width="13" height="13" viewBox="0 0 13 13"><circle cx="6.5" cy="6.5" r="5.5" fill="none" stroke="#fff" stroke-width="1.4"/><path d="M4 6.6l1.8 1.8L9.2 5" fill="none" stroke="#fff" stroke-width="1.4"/></svg>We are Accessable 7 days a week</li>
    <li><svg width="13" height="13" viewBox="0 0 13 13"><circle cx="6.5" cy="6.5" r="5.5" fill="none" stroke="#fff" stroke-width="1.4"/><path d="M4 6.6l1.8 1.8L9.2 5" fill="none" stroke="#fff" stroke-width="1.4"/></svg>We constantly upskill to keep up with changes to tax laws and legislation</li>
    <li><svg width="13" height="13" viewBox="0 0 13 13"><circle cx="6.5" cy="6.5" r="5.5" fill="none" stroke="#fff" stroke-width="1.4"/><path d="M4 6.6l1.8 1.8L9.2 5" fill="none" stroke="#fff" stroke-width="1.4"/></svg>Our advise is explained in plain english so you understand</li>
    <li><svg width="13" height="13" viewBox="0 0 13 13"><circle cx="6.5" cy="6.5" r="5.5" fill="none" stroke="#fff" stroke-width="1.4"/><path d="M4 6.6l1.8 1.8L9.2 5" fill="none" stroke="#fff" stroke-width="1.4"/></svg>Our fees are not only fair but very competitive</li>
    <li><svg width="13" height="13" viewBox="0 0 13 13"><circle cx="6.5" cy="6.5" r="5.5" fill="none" stroke="#fff" stroke-width="1.4"/><path d="M4 6.6l1.8 1.8L9.2 5" fill="none" stroke="#fff" stroke-width="1.4"/></svg>We don't believe in one size fits all, we listen to client's challenges indiviually</li>
    <li><svg width="13" height="13" viewBox="0 0 13 13"><circle cx="6.5" cy="6.5" r="5.5" fill="none" stroke="#fff" stroke-width="1.4"/><path d="M4 6.6l1.8 1.8L9.2 5" fill="none" stroke="#fff" stroke-width="1.4"/></svg>Our level of service and work ethics is no different to any other large CA practices</li>
    <li><svg width="13" height="13" viewBox="0 0 13 13"><circle cx="6.5" cy="6.5" r="5.5" fill="none" stroke="#fff" stroke-width="1.4"/><path d="M4 6.6l1.8 1.8L9.2 5" fill="none" stroke="#fff" stroke-width="1.4"/></svg>We have affiliations with other business partners</li>
    <li><svg width="13" height="13" viewBox="0 0 13 13"><circle cx="6.5" cy="6.5" r="5.5" fill="none" stroke="#fff" stroke-width="1.4"/><path d="M4 6.6l1.8 1.8L9.2 5" fill="none" stroke="#fff" stroke-width="1.4"/></svg>We keep up with everchanging cloud based technology</li>
  </ul>
</section>
<div class="abs why-photo" role="img" aria-label="Top view of hands with calculators, binders and documents on a white desk"></div>

<h2 class="abs section-title" style="top:1944px">WHAT <em>CLIENTS</em> SAY</h2>
<div class="abs hand-left" role="img" aria-label="Hand making an OK gesture"></div>
<div class="abs hand-right" role="img" aria-label="Hand making an OK gesture"></div>
<div class="abs tagline">Don’t take<br><em>our word</em><br>for it</div>
<div class="abs quote">
  <p>“Lorem ipsum dolor sit amet, consectetur adipiscing elit, sed do eiusmod tempor incididunt ut labore et dolore magna aliqua. Ut enim ad minim ipsum dolor sit amet, consectetur adipiscing elit, sed do eiusmod temporaliqua.”</p>
  <h4>John Doe</h4>
  <span>Company name</span>
</div>
<div class="abs arrow" style="left:300px">‹</div>
<div class="abs arrow" style="left:891px">›</div>

<h2 class="abs section-title" style="top:2645px">INDUSTRIES <em>WE REPRESENT</em></h2>
<svg width="0" height="0" style="position:absolute"><defs>
  <g id="ring"><path d="M44 10 A29 29 0 1 0 44 50" fill="none" stroke="#4a9b3f" stroke-width="3"/><circle cx="30" cy="30" r="22" fill="none" stroke="#4a9b3f" stroke-width="1.2" stroke-dasharray="3 2"/><rect x="21" y="21" width="18" height="18" rx="3" fill="none" stroke="#4a9b3f" stroke-width="1.6"/></g>
</defs></svg>
<div class="abs industry" style="left:109px;top:2724px"><svg width="60" height="60"><use href="#ring"/></svg>Healthcare Specialists</div>
<div class="abs industry" style="left:361px;top:2724px"><svg width="60" height="60"><use href="#ring"/></svg>Construction</div>
<div class="abs industry" style="left:613px;top:2724px"><svg width="60" height="60"><use href="#ring"/></svg>Professional Services</div>
<div class="abs industry" style="left:884px;top:2724px"><svg width="60" height="60"><use href="#ring"/></svg>Legal</div>
<div class="abs industry" style="left:109px;top:2810px"><svg width="60" height="60"><use href="#ring"/></svg>Contractors</div>
<div class="abs industry" style="left:361px;top:2810px"><svg width="60" height="60"><use href="#ring"/></svg>Architecture</div>
<div class="abs industry" style="left:613px;top:2810px"><svg width="60" height="60"><use href="#ring"/></svg>Retail</div>
<div class="abs industry" style="left:884px;top:2810px"><svg width="60" height="60"><use href="#ring"/></svg>Medical Practinioners</div>
<div class="abs industry" style="left:109px;top:2896px"><svg width="60" height="60"><use href="#ring"/></svg>Manufacturing</div>
<div class="abs industry" style="left:361px;top:2896px"><svg width="60" height="60"><use href="#ring"/></svg>Real Estate Rentals</div>
<div class="abs industry" style="left:613px;top:2896px"><svg width="60" height="60"><use href="#ring"/></svg>Childcare</div>
<div class="abs industry" style="left:884px;top:2896px"><svg width="60" height="60"><use href="#ring"/></svg>Film Industry</div>

<footer class="abs site-footer">
  <div class="subscribe"><span>Email address</span><b>SUBSCRIBE</b></div>
  <h3 class="f-head" style="left:139px">Links</h3>
  <ul class="f-list" style="left:139px"><li>Home</li><li>Services</li><li>Testimonials</li><li>Contact</li></ul>
  <div class="f-rule" style="left:336px"></div>
  <h3 class="f-head" style="left:462px">Contact us</h3>
  <ul class="f-list" style="left:462px">
    <li><svg width="14" height="14" viewBox="0 0 14 14"><path d="M7 1a4 4 0 0 1 4 4c0 3-4 8-4 8S3 8 3 5a4 4 0 0 1 4-4z" fill="#fff"/><circle cx="7" cy="5" r="1.5" fill="#000"/></svg><span>P O Box 50721, Eastfield, Auckland<br>2190</span></li>
    <li><svg width="14" height="14" viewBox="0 0 14 14"><path d="M3 1l3 3-1.5 2a8 8 0 0 0 3.5 3.5L10 8l3 3-2 2C6 13 1 8 1 3z" fill="#fff"/></svg>021 555 0184</li>
    <li><svg width="14" height="14" viewBox="0 0 14 14"><rect x="1" y="3" width="12" height="9" fill="#fff"/><path d="M1 3l6 5 6-5" fill="none" stroke="#000" stroke-width="1.2"/></svg>info@harbourlinetax.co.nz</li>
  </ul>
  <div class="f-rule" style="left:817px"></div>
  <h3 class="f-head" style="left:944px">Follow us</h3>
  <div class="socials"><span aria-label="Social link"></span><span aria-label="Social link"></span><span aria-label="Social link"></span><span aria-label="Social link"></span></div>
  <p class="copyright">© Copyrights.2022.The Company Name.All Rights Reserved</p>
</footer>

</body>
</html>
```